Stationary and document suite for consultancy business in Australia called Lumara

I would like to get a suite of documents suitable for my new business called Lumara. I have included the original brief below, however have already selected a design for the logo. I would like to get:
Letter head - simple letter template with "V" logo embossed in background
Word document - standard format with "V" logo embossed in background
Proposal document - bolder pages with cover and back cover, include empty pages with footer as well as contents
Powerpoint presentation - open to ideas
Email signature - banner style or text, open to ideas
Brief that was given for logo (logo not required)
The name of the business is derived from the latin word for green ("Viridis") combined with "co" which is intended to represent a number of different words: collaborative, cooperative, coaching, collective,  construction, consulting, etc.
My objective for the brand is to represent a dynamic, progressive and collaborative business, where our people have fun and enjoy their work.
The objective of our business is to provide consultancy services to construction businesses, mainly aimed at building high performing teams and strategic growth. We will create learning and development tools that businesses can use to increase staff satisfaction and retention. Our future goal is to invest in decarbonisation and sustainability technology for use in the construction industry.
Our target market is construction business leaders and infrastructure owners, who operate road, rail and utility assets. We also want to present as a dynamic, progressive and fun place to work that will be attractive to new employees.

```html
<!DOCTYPE html>
<html lang="en">
<head>
<meta charset="utf-8">
<title>Lumara Stationery Suite</title>
<link href="https://fonts.googleapis.com/css2?family=Poppins:wght@400;500;600;700&display=swap" rel="stylesheet">
<style>
:root{
  --green:#8cc63f;
  --dark:#3d3d3f;
  --grey:#6d6e71;
  --photo:#4b4849;
  --bg-top:#e6e7e9;
  --bg-main:#d8d9db;
  --paper:#fdfdfd;
  --body-text:#8a8b8d;
}
*{margin:0;padding:0;box-sizing:border-box}
html,body{width:1200px;height:2526px;overflow:hidden}
body{font-family:'Poppins',sans-serif;background:var(--bg-main);position:relative;color:var(--dark)}
.band-top{position:absolute;left:0;top:0;width:1200px;height:798px;background:var(--bg-top)}
.sheet{position:absolute;background:var(--paper);box-shadow:3px 5px 10px rgba(0,0,0,.28)}
.letter{top:112px;width:412px;height:572px}
.letter.blank{left:164px}
.letter.filled{left:613px;width:408px}
.footer-bar{position:absolute;left:0;right:0;bottom:0;height:7px;background:var(--dark)}
.footer-bar::after{content:"";position:absolute;right:0;top:0;height:7px;width:110px;background:var(--green);clip-path:polygon(8px 0,100% 0,100% 100%,0 100%)}
.brand{position:absolute;display:flex;align-items:center;gap:8px;font-weight:500;color:var(--grey);letter-spacing:1px}
.brand .dot{border-radius:50%;background:var(--green);flex:none}
.letter .brand{left:36px;top:40px;font-size:34px}
.letter .brand .dot{width:14px;height:14px}
.contact-block{position:absolute;left:250px;top:34px;font-size:7.5px;line-height:10.5px;color:var(--dark)}
.letter.filled .contact-block{left:248px}
.contact-block .ico{display:inline-block;width:6px;height:6px;background:var(--green);border-radius:50%;margin-right:3px}
.letter-body{position:absolute;left:36px;top:132px;width:340px;font-size:7px;line-height:11px;color:var(--body-text);text-align:justify}
.letter-body p{margin-bottom:11px}
.signature{width:50px;height:40px;background:linear-gradient(135deg,#eceef3,#dfe3ec);margin-top:4px}
.slide{width:388px;height:295px}
.s-l{left:196px}.s-r{left:617px}
.r1{top:925px}.r2{top:1253px}.r3{top:1579px}
.cover-title{position:absolute;left:0;right:0;text-align:center}
.cover .brand{left:0;right:0;justify-content:center;top:88px;font-size:50px}
.cover .brand .dot{width:18px;height:18px}
.welcome{top:196px;font-size:14px;font-weight:500}
.pres-name{top:220px;font-size:20px;font-weight:600;color:var(--green)}
.desc{top:246px;font-size:14px;font-weight:500}
.slide-head{position:absolute;left:26px;top:46px}
.slide-head h2{font-size:15px;font-weight:600;color:var(--green);line-height:18px}
.slide-head span{font-size:8.5px;color:var(--grey);display:block;line-height:10px}
.head-rule{position:absolute;left:88px;right:26px;top:70px;height:1px;background:var(--grey)}
.slide .brand.mini{right:26px;top:34px;font-size:13px;gap:5px}
.slide .brand.mini .dot{width:8px;height:8px}
.team{position:absolute;left:26px;top:98px;display:flex;gap:9px}
.member{width:77px}
.photo{height:78px;background:var(--photo);color:#fff;font-size:9px;display:flex;align-items:center;justify-content:center}
.member h3{font-size:9px;font-weight:500;color:var(--green);margin-top:14px;line-height:10px}
.member .role{font-size:8px;color:var(--grey);line-height:10px}
.tiny{font-size:4px;line-height:5.5px;color:var(--body-text);text-align:justify}
.member .tiny{margin-top:6px}
.groups{position:absolute;left:26px;top:88px;width:336px;display:grid;grid-template-columns:1fr 1fr;column-gap:18px;row-gap:12px}
.groups h4{font-size:6px;font-weight:600;color:var(--dark);line-height:8px}
.chart{position:absolute;left:26px;top:82px}
.chart-note{position:absolute;left:20px;top:210px;width:350px}
.pie-text{position:absolute;left:26px;top:90px;width:160px}
.pie{position:absolute;left:220px;top:78px}
.pie-lower{position:absolute;left:26px;top:210px;width:336px;display:grid;grid-template-columns:1fr 1fr;gap:18px}
.thanks{background:var(--green);color:#fff;text-align:center}
.thanks h2{position:absolute;left:0;right:0;top:70px;font-size:40px;font-weight:500;line-height:50px}
.thanks .fine{position:absolute;left:0;right:0;top:224px;font-size:8.5px;line-height:13px}
.card{left:259px;top:2138px;width:682px;height:250px}
.card .name{position:absolute;left:45px;top:40px;font-size:24px;font-weight:600;color:var(--dark);letter-spacing:.3px}
.card .title{position:absolute;left:45px;top:70px;font-size:20px;color:var(--green)}
.card .lines{position:absolute;left:45px;top:140px;font-size:20px;line-height:26px;color:var(--dark)}
.card .lines svg{vertical-align:-2px;margin-right:6px}
.card .brand{left:330px;top:110px;font-size:60px}
.card .brand .dot{width:22px;height:22px}
.card-bar{position:absolute;left:0;right:0;bottom:0;height:16px;background:var(--dark)}
.card-bar::after{content:"";position:absolute;right:0;top:0;height:16px;width:200px;background:var(--green);clip-path:polygon(16px 0,100% 0,100% 100%,0 100%)}
</style>
</head>
<body>
<div class="band-top"></div>

<!-- Letterhead, blank -->
<section class="sheet letter blank">
  <div class="brand"><span class="dot"></span>Lumara</div>
  <div class="contact-block">14 Harbour View Road<br>Richmond Hill, ON L4S 1A1<br><span class="ico"></span>+61 400 555 018<br><span class="ico"></span>marcus@lumara.com.au<br><span class="ico"></span>www.lumara.com.au</div>
  <div class="footer-bar"></div>
</section>

<!-- Letterhead, with letter -->
<section class="sheet letter filled">
  <div class="brand"><span class="dot"></span>Lumara</div>
  <div class="contact-block">14 Harbour View Road<br>Richmond Hill, ON L4S 1A1<br><span class="ico"></span>+61 400 555 018<br><span class="ico"></span>marcus@lumara.com.au<br><span class="ico"></span>www.lumara.com.au</div>
  <div class="letter-body">
    <p>Dear customer,</p>
    <p>Lorem ipsum dolor sit amet, consectetur adipiscing elit, sed do eiusmod tempor incididunt ut labore et dolore magna aliqua. Ut enim ad minim veniam, quis nostrud exercitation ullamco laboris nisi ut aliquip ex ea commodo consequat. Duis aute irure dolor in reprehenderit in voluptate velit esse cillum dolore eu fugiat nulla pariatur. Excepteur sint occaecat cupidatat non proident, sunt in culpa qui officia deserunt mollit anim id est laborum.</p>
    <p>Lorem ipsum dolor sit amet, consectetur adipiscing elit, sed do eiusmod tempor incididunt ut labore et dolore magna aliqua. Ut enim ad minim veniam, quis nostrud exercitation ullamco laboris nisi ut aliquip ex ea commodo consequat. Duis aute irure dolor in reprehenderit in voluptate velit esse cillum dolore eu fugiat nulla pariatur. Excepteur sint occaecat cupidatat non proident, sunt in culpa qui officia deserunt mollit anim id est laborum.</p>
    <p>Lorem ipsum dolor sit amet, consectetur adipiscing elit, sed do eiusmod tempor incididunt ut labore et dolore magna aliqua. Ut enim ad minim veniam, quis nostrud exercitation ullamco laboris nisi ut aliquip ex ea commodo consequat. Duis aute irure dolor in reprehenderit in voluptate velit esse cillum dolore eu fugiat nulla pariatur. Excepteur sint occaecat cupidatat non proident, sunt in culpa qui officia deserunt mollit anim id est laborum.</p>
    <p>Lorem ipsum dolor sit amet, consectetur adipiscing elit, sed do eiusmod tempor incididunt ut labore et dolore magna aliqua. Ut enim ad minim veniam, quis nostrud exercitation ullamco laboris nisi ut aliquip ex ea commodo consequat. Duis aute irure dolor in reprehenderit.</p>
    <p style="margin-bottom:4px">Yours Sincerely,</p>
    <div class="signature" role="img" aria-label="Handwritten signature"></div>
  </div>
  <div class="footer-bar"></div>
</section>

<!-- Slide: cover -->
<section class="sheet slide s-l r1 cover">
  <div class="brand"><span class="dot"></span>Lumara</div>
  <div class="cover-title welcome">Welcome to Our</div>
  <div class="cover-title pres-name">Presentation Name</div>
  <div class="cover-title desc">Drescription</div>
</section>

<!-- Slide: team -->
<section class="sheet slide s-r r1">
  <div class="slide-head"><h2>Heading Here</h2><span>Sub Heading</span></div>
  <div class="head-rule"></div>
  <div class="brand mini"><span class="dot"></span>Lumara</div>
  <div class="team">
    <div class="member"><div class="photo" role="img" aria-label="Team member portrait">Photo</div><h3>Team Member1</h3><div class="role">Title</div><p class="tiny">Short profile text about this team member, their role, skills and years of project experience.</p></div>
    <div class="member"><div class="photo" role="img" aria-label="Team member portrait">Photo</div><h3>Team Member1</h3><div class="role">Title</div><p class="tiny">Short profile text about this team member, their role, skills and years of project experience.</p></div>
    <div class="member"><div class="photo" role="img" aria-label="Team member portrait">Photo</div><h3>Team Member1</h3><div class="role">Title</div><p class="tiny">Short profile text about this team member, their role, skills and years of project experience.</p></div>
    <div class="member"><div class="photo" role="img" aria-label="Team member portrait">Photo</div><h3>Team Member1</h3><div class="role">Title</div><p class="tiny">Short profile text about this team member, their role, skills and years of project experience.</p></div>
  </div>
</section>

<!-- Slide: groups -->
<section class="sheet slide s-l r2">
  <div class="slide-head"><h2>Heading Here</h2><span>Sub Heading</span></div>
  <div class="head-rule"></div>
  <div class="brand mini"><span class="dot"></span>Lumara</div>
  <div class="groups">
    <div><h4>Group 1</h4><p class="tiny">Placeholder copy for this group describing the service area, its goals and the outcomes clients can expect from the program.</p></div>
    <div><h4>Group 1</h4><p class="tiny">Placeholder copy for this group describing the service area, its goals and the outcomes clients can expect from the program.</p></div>
    <div><h4>Group 1</h4><p class="tiny">Placeholder copy for this group describing the service area, its goals and the outcomes clients can expect from the program.</p></div>
    <div><h4>Group 1</h4><p class="tiny">Placeholder copy for this group describing the service area, its goals and the outcomes clients can expect from the program.</p></div>
    <div><h4>Group 1</h4><p class="tiny">Placeholder copy for this group describing the service area, its goals and the outcomes clients can expect from the program.</p></div>
    <div><h4>Group 1</h4><p class="tiny">Placeholder copy for this group describing the service area, its goals and the outcomes clients can expect from the program.</p></div>
  </div>
</section>

<!-- Slide: bar chart -->
<section class="sheet slide s-r r2">
  <div class="slide-head"><h2>Heading Here</h2><span>Sub Heading</span></div>
  <div class="head-rule"></div>
  <div class="brand mini"><span class="dot"></span>Lumara</div>
  <svg class="chart" width="336" height="120" viewBox="0 0 336 120">
    <g stroke="#e3e3e3" stroke-width=".6">
      <line x1="6" y1="14" x2="336" y2="14"/><line x1="6" y1="28" x2="336" y2="28"/><line x1="6" y1="42" x2="336" y2="42"/><line x1="6" y1="56" x2="336" y2="56"/><line x1="6" y1="70" x2="336" y2="70"/><line x1="6" y1="84" x2="336" y2="84"/>
    </g>
    <line x1="6" y1="98" x2="336" y2="98" stroke="#bbb" stroke-width=".6"/>
    <g fill="#8cc63f"><rect x="24" y="46" width="9" height="52"/><rect x="64" y="58" width="9" height="40"/><rect x="102" y="44" width="9" height="54"/><rect x="120" y="60" width="9" height="38"/><rect x="164" y="56" width="9" height="42"/><rect x="196" y="48" width="9" height="50"/><rect x="230" y="44" width="9" height="54"/><rect x="274" y="40" width="9" height="58"/><rect x="292" y="46" width="9" height="52"/></g>
    <g fill="#808285"><rect x="37" y="66" width="9" height="32"/><rect x="136" y="70" width="9" height="28"/><rect x="182" y="74" width="9" height="24"/><rect x="246" y="64" width="9" height="34"/></g>
    <g fill="#231f20"><rect x="50" y="70" width="9" height="28"/><rect x="150" y="74" width="9" height="24"/></g>
    <g fill="#aaa" font-size="3.5" font-family="Poppins, sans-serif">
      <text x="44" y="106">2019</text><text x="128" y="106">2020</text><text x="208" y="106">2021</text><text x="284" y="106">2022</text>
      <text x="26" y="116">■ Channel A</text><text x="70" y="116">■ Channel B</text><text x="118" y="116">■ Channel C</text><text x="166" y="116">■ Channel D</text>
    </g>
  </svg>
  <p class="tiny chart-note">Placeholder summary for the chart above describing growth across each channel over four years, key trends in engagement, notable peaks in the latest year, and how results compare against the original targets set in the strategic plan. Further notes outline next steps, priorities and the measures the team will track to keep momentum going through the coming period.</p>
</section>

<!-- Slide: pie chart -->
<section class="sheet slide s-l r3">
  <div class="slide-head"><h2>Heading Here</h2><span>Sub Heading</span></div>
  <div class="head-rule"></div>
  <div class="brand mini"><span class="dot"></span>Lumara</div>
  <p class="tiny pie-text">Placeholder paragraph describing the breakdown shown in the chart, with notes on sales, revenue, profit and expenditure for the period, key drivers behind each share, and a short comment on what the figures mean for planning and investment decisions in the year ahead.</p>
  <svg class="pie" width="140" height="120" viewBox="0 0 140 120">
    <circle cx="64" cy="52" r="48" fill="#8cc63f"/>
    <path d="M64 52 L34 14.5 A48 48 0 0 1 99 19 Z" fill="#a8a592"/>
    <path d="M64 52 L99 19 A48 48 0 0 1 107 74 Z" fill="#243238"/>
    <g font-size="4" fill="#fff" font-family="Poppins, sans-serif"><text x="60" y="22">25%</text><text x="92" y="52">15%</text><text x="40" y="70">60%</text></g>
    <g font-size="4.5" fill="#555" font-family="Poppins, sans-serif"><text x="12" y="110">■ Sale  ■ Revenue  ■ Profit  ■ Expenditure</text></g>
  </svg>
  <div class="pie-lower">
    <p class="tiny">Placeholder note with further detail on the figures, the period covered and the sources used to prepare this summary.</p>
    <p class="tiny">Placeholder note with further detail on the figures, the period covered and the sources used to prepare this summary.</p>
  </div>
</section>

<!-- Slide: closing -->
<section class="sheet slide s-r r3 thanks">
  <h2>Thanks<br>For Wathing</h2>
  <div class="fine">P : +61 400 555 018  E : marcus@lumara.com.au<br>14 Harbour View Road, Richmond Hill, ON L4S 1A1<br>www.lumara.com.au</div>
</section>

<!-- Business card -->
<section class="sheet card">
  <div class="name">MARCUS ELLERY</div>
  <div class="title">Director</div>
  <div class="lines">
    <div><svg width="18" height="16" viewBox="0 0 18 16"><path d="M2 6 Q9 0 16 6 L14 8 L12 6 L6 6 L4 8 Z M4 9 H14 L15 15 H3 Z" fill="#8cc63f"/></svg>+61 400 555 018</div>
    <div><svg width="18" height="14" viewBox="0 0 18 14"><rect x="1" y="1" width="16" height="12" fill="#8cc63f"/><path d="M1 1 L9 8 L17 1" stroke="#fff" stroke-width="1.5" fill="none"/></svg>marcus@lumara.com.au</div>
    <div><svg width="18" height="18" viewBox="0 0 18 18"><circle cx="9" cy="9" r="8" fill="#8cc63f"/><path d="M5 5 Q9 8 7 12 M11 4 Q13 9 12 14" stroke="#fff" stroke-width="1.4" fill="none"/></svg>www.lumara.com.au</div>
  </div>
  <div class="brand"><span class="dot"></span>Lumara</div>
  <div class="card-bar"></div>
</section>
</body>
</html>
```